DOG DAYCARE BILLBOARD

Design a bold exciting billboard that can be read easily from a distance! Our goal is brand awareness and showcasing the services we offer (Boarding, Grooming, Daycare, and Training.
we would like to see examples with the phrase "your best friend's best day". Our name Bright Meadow Canine Activity Center (or just Bright Meadow might work better and could be bigger) and the services we provide.
(there are two examples of what we like included in the pictures)
you can find more information o our website at pawplayhub@mailnest.example.

```html
<!DOCTYPE html>
<html lang="en">
<head>
<meta charset="utf-8">
<title>Bright Meadow Billboard</title>
<link rel="stylesheet" href="https://fonts.googleapis.com/css2?family=Quicksand:wght@400;700&family=PT+Serif:ital,wght@1,700&family=Montserrat:wght@700&display=swap">
<style>
  :root {
    --gold: #c8b900;
    --navy: #28406f;
    --navy-deep: #1d2f57;
    --white: #ffffff;
    --sheen: #e4e4e4;
    --stage: #d9d9d9;
    --ink: #111111;
  }
  * { box-sizing: border-box; margin: 0; padding: 0; }
  html, body { width: 975px; height: 1200px; overflow: hidden; }
  body {
    background: var(--stage);
    position: relative;
    font-family: "Quicksand", sans-serif;
  }
  .billboard {
    position: absolute;
    left: 37px;
    top: 400px;
    width: 900px;
    height: 416px;
    background: var(--white);
    box-shadow: 0 6px 18px rgba(0,0,0,0.25);
  }
  .billboard-shapes {
    position: absolute;
    inset: 0;
    width: 900px;
    height: 416px;
  }
  .dog-photo {
    position: absolute;
    left: 43px;
    top: -43px;
    width: 528px;
    height: 277px;
    border-radius: 48% 48% 40% 40% / 60% 60% 30% 30%;
    background: radial-gradient(ellipse at 55% 45%, #c9843f 0%, #d79a58 40%, rgba(230,180,120,0.5) 70%, rgba(255,255,255,0) 100%);
  }
  .brand {
    position: absolute;
    left: 585px;
    top: 95px;
    width: 270px;
    display: flex;
    align-items: center;
    gap: 10px;
  }
  .brand-mark {
    width: 22px;
    height: 22px;
    border-radius: 50%;
    background: var(--ink);
    flex: none;
  }
  .brand-name {
    font-family: "Quicksand", sans-serif;
    font-weight: 700;
    font-size: 34px;
    color: var(--ink);
    white-space: nowrap;
    line-height: 1;
  }
  .services {
    position: absolute;
    left: 0;
    width: 100%;
    top: 252px;
    text-align: center;
    font-size: 37px;
    font-weight: 700;
    color: var(--white);
    letter-spacing: 0.2px;
    line-height: 1;
  }
  .services .joiner { font-weight: 400; }
  .tagline {
    position: absolute;
    left: 232px;
    top: 313px;
    width: 440px;
    text-align: center;
    font-family: "PT Serif", serif;
    font-style: italic;
    font-weight: 700;
    font-size: 29px;
    color: var(--white);
    line-height: 1;
  }
  .contact-row {
    position: absolute;
    left: 0;
    width: 100%;
    top: 370px;
    display: flex;
    justify-content: center;
    align-items: center;
    gap: 20px;
    font-family: "Montserrat", sans-serif;
    font-weight: 700;
    font-size: 16.5px;
    color: var(--navy-deep);
    white-space: nowrap;
  }
  .contact-item { display: flex; align-items: center; gap: 6px; }
  .contact-item svg { width: 16px; height: 16px; flex: none; }
  .divider { width: 1.5px; height: 16px; background: var(--navy-deep); }
  .accent { color: var(--gold); }
</style>
</head>
<body>
  <div class="billboard">
    <svg class="billboard-shapes" viewBox="0 0 900 416" aria-hidden="true">
      <defs>
        <linearGradient id="sheen" x1="0" y1="0" x2="1" y2="1">
          <stop offset="0" stop-color="#ffffff"/>
          <stop offset="1" stop-color="#dcdcdc"/>
        </linearGradient>
      </defs>
      <path d="M560 0 L900 0 L900 109 C 800 160, 700 190, 560 210 Z" fill="url(#sheen)" opacity="0.7"/>
      <path d="M0 195 C 220 270, 600 265, 900 109 L900 337 L0 337 Z" fill="var(--gold)"/>
      <rect x="0" y="336" width="900" height="4" fill="var(--navy-deep)"/>
      <path d="M232 310 L692 310 L682 357 L222 357 Z" fill="var(--navy)"/>
      <path d="M222 357 L682 357 L681 360 L221 360 Z" fill="var(--gold)"/>
    </svg>

    <div class="dog-photo" role="img" aria-label="Photo of a smiling golden retriever lying down"></div>

    <div class="brand">
      <span class="brand-mark"></span>
      <span class="brand-name">Bright Meadow</span>
    </div>

    <p class="services">Boarding, Grooming, Daycare, <span class="joiner">and</span> Training</p>
    <p class="tagline">your best friend's best day</p>

    <div class="contact-row">
      <span class="contact-item">
        <svg viewBox="0 0 16 16" fill="none" stroke="var(--gold)" stroke-width="1.3"><circle cx="8" cy="8" r="6.5"/><ellipse cx="8" cy="8" rx="3" ry="6.5"/><line x1="1.5" y1="8" x2="14.5" y2="8"/><line x1="2.5" y1="4.5" x2="13.5" y2="4.5"/><line x1="2.5" y1="11.5" x2="13.5" y2="11.5"/></svg>
        BrightMeadowDogs.example
      </span>
      <span class="divider"></span>
      <span class="contact-item">
        <svg viewBox="0 0 16 16" fill="none" stroke="var(--gold)" stroke-width="1.3"><circle cx="8" cy="8" r="6.8"/><path d="M5.5 4.5 L7 4.3 L7.6 6.3 L6.7 7 C7.1 8 7.9 8.9 9 9.4 L9.7 8.5 L11.6 9.1 L11.5 10.6 C8.3 11 5 7.7 5.5 4.5 Z"/></svg>
        (555) 014-2760
      </span>
      <span class="divider"></span>
      <span class="contact-item">
        <svg viewBox="0 0 16 16" fill="none" stroke="var(--gold)" stroke-width="1.3"><circle cx="8" cy="5.5" r="3.5"/><line x1="8" y1="9" x2="8" y2="14"/><line x1="5" y1="14.5" x2="11" y2="14.5"/></svg>
        <span><span class="accent">VISIT US IN</span> MAPLE RIDGE, IA</span>
      </span>
    </div>
  </div>
</body>
</html>
```